Affiliate website design and wireframe

We need a design of an affiliate website for an application we purchased, it is important that you build the website pages according to the developer of the applications specifications (please see attached documents) the developer of the application will configure the pages and add them to the site. Please take special note of his comments below.

We all so need you to create a wire frame so the developer can test everything (http://quartz.lomeriva.vn/)

It will be the homepage and about 16 inner pages (please see attached files)
Here is our website http://maplecourtlink.com/affiliate/affiliates/index.php

The version of the software we purchased is the Quill Partner Grid version

Comments from the developers

1. I will need the source files of the design (photoshop .psd files and font files if custom fonts are used), since the implementation is closely bound to component sizes (like border width, margin width etc.) and colors. If you own a corporate design manual, it's crucial to send it as well. Also, please, make sure if you use custom fonts, that these allow legal website integration (like zorvix web fonts).

2. Any and every content is controlled via templates. All editing/adding/removing etc. is done here. The template files are essentially html/php documents, they use a template engine called brisko (http://www.brisko.net/) which has it's own language similar to php.

3. .psd files are ideal, because we deal with the specifics of QPS/QPG implementation on a daily basis. Any html/css developed in advance may prove to be a poor choice. You may choose to let an in-house developer do the job, but experience wise this is more costly, since he will not be accustomed to the template/functionality systems of QPS/QPG.

4. I will need the source files of the design (photoshop .psd files and font files if custom fonts are used), since the implementation is closely bound to component sizes (like border width, margin width etc.) and colors. If you own a corporate design manual, it's crucial to send it as well. Also, please, make sure if you use custom fonts, that these allow legal website integration (like zorvix web fonts).

Regards,

Tomas Vereck

We prefer illustrations more than pictures of real people.

This is the home page, it is asking for Merchant and Affiliate sign up, not just affiliate.

http://maplecourtlink.com/affiliate/index.php

Please note the home page features both Merchant and Affiliate sign up

We are looking for illustration design not just stock images

Please remember the search menu that searches for the available programs, see the example we gave you, look at the search menu at the top of the page http://www.tradolink.com/

We are reviewing everything, no need to send more designs

Target Market(s)

Natural Products Manufacturers
Natural products Sales reps
Natural Products Bloggers
Social Marketing

Industry/Entity Type

Software

Requirements
Must have
• 1. All links on pages should go to the appropriate pages.
2. Colors can be based on our logo design (look at the attachments)
3. Here is our website http://maplecourtlink.com/affiliate/affiliates/index.php
4. We have attached a drawing of how we think the homepage concept should follow.
5. Main concept of design, is trying to show our sales people (Affiliates) are doing multiple things to advertise and sell the merchants products.(see logo)
6. Need to be able to edit all text and images.
7. Our target audience is Natural product sales people (Advertisers, bloggers, ext) and natural product manufacturers.
8. You can speak to the company who made the application, through live chat, on there website http://www.quillpartnergrid.com/
Nice to have
• See Attached Documents.
site should take up whole website pages
Look For fun Illustrated Website, one of the better ones we have seen is http://www.tradolink.com/index.cfm
Should not have
• Please look very carefully at developers comment above.

```html
<!DOCTYPE html>
<html lang="en">
<head>
<meta charset="utf-8">
<title>Maplecourt Link – Affiliate Program</title>
<link rel="stylesheet" href="https://fonts.googleapis.com/css2?family=Ubuntu:wght@400;500;700&family=Open+Sans:wght@400;600&display=swap">
<style>
:root{
  --green:#5ca61c;
  --green-dark:#3f7f10;
  --green-light:#8fd13a;
  --navy:#0c2f5e;
  --ink:#222;
  --text:#555;
  --grey-bg:#f1f1f1;
  --line:#d6d6d6;
  --footer:#0d1926;
  --footer-bar:#08111b;
  --white:#fff;
}
*{box-sizing:border-box;margin:0;padding:0}
html,body{width:1200px;height:3341px;overflow:hidden}
body{font-family:"Open Sans",Arial,sans-serif;color:var(--text);background:var(--white);position:relative}
h1,h2,h3,h4{font-family:"Ubuntu",Arial,sans-serif}
a{color:inherit;text-decoration:none}
section,header,footer{position:absolute;left:0;width:1200px}

/* header */
.site-header{top:0;height:139px}
.brand{position:absolute;left:50px;top:30px;display:flex;align-items:center;gap:12px}
.brand-mark{width:46px;height:46px;border-radius:50%;background:var(--green)}
.brand-name{font-family:"Ubuntu",sans-serif;font-weight:700;font-size:24px;color:var(--navy)}
.top-links{position:absolute;right:50px;top:8px;font-size:12px;color:#666}
.top-links a{padding:0 4px}
.login{position:absolute;top:42px;right:50px;display:flex;gap:12px}
.btn{display:inline-block;font-family:"Ubuntu",sans-serif;font-weight:500;font-size:13px;color:var(--white);padding:0 16px;height:33px;line-height:33px;border-radius:2px;text-transform:uppercase}
.btn-green{background:var(--green)}
.btn-navy{background:var(--navy)}
.main-nav{position:absolute;left:50px;right:50px;top:100px;display:flex;justify-content:space-between;font-family:"Ubuntu",sans-serif;font-size:14px;color:var(--green);text-transform:uppercase;border-bottom:1px solid #e3e3e3;height:32px}
.main-nav a{position:relative}
.main-nav a.active::after{content:"";position:absolute;left:0;right:0;bottom:-9px;height:3px;background:var(--green)}

/* hero */
.hero{top:139px;height:649px;background:radial-gradient(ellipse at 50% 55%,#a6e65a 0%,#5cb51e 45%,#2f7d0c 100%);overflow:hidden}
.hero-title{position:absolute;top:38px;width:100%;text-align:center;color:var(--white);font-size:40px;font-weight:700;letter-spacing:.5px}
.hero-title span{color:#f7ec5c}
.hero-lines{position:absolute;inset:0}
.hub{position:absolute;left:475px;top:270px;width:250px;height:250px;border-radius:50%;background:radial-gradient(circle,#f6e7a0,#d9a53a 70%,#b9862a);}
.node{position:absolute;width:134px;height:134px;border-radius:50%;background:var(--white);box-shadow:0 4px 12px rgba(0,0,0,.25);display:flex;align-items:center;justify-content:center}
.node .fill{width:80px;height:80px;border-radius:50%}
.hero-cta{position:absolute;left:489px;top:557px;width:222px;height:50px;line-height:50px;text-align:center;background:#111;color:var(--white);font-family:"Ubuntu",sans-serif;font-weight:700;font-size:16px;border-radius:3px;text-transform:uppercase}

/* programs */
.programs{top:788px;height:356px;display:flex}
.program{width:600px;height:356px;padding:68px 50px 0;color:var(--white)}
.program-affiliate{background:var(--navy)}
.program-merchant{background:var(--green)}
.program h2{font-size:24px;font-weight:500;text-transform:uppercase;margin-bottom:26px}
.program p{font-size:13px;line-height:21px;max-width:480px}
.program .btn{margin-top:30px;height:32px;line-height:32px;font-size:12px}
.program-affiliate .btn{background:var(--green)}
.program-merchant .btn{background:var(--navy)}

/* section headings */
.sec-title{text-align:center;font-size:22px;font-weight:500;color:var(--ink);text-transform:uppercase;position:relative}
.sec-title::after{content:"";display:block;width:60px;height:3px;background:var(--green);margin:14px auto 0}

.welcome{top:1144px;height:331px;padding-top:72px}
.welcome p{width:1100px;margin:40px auto 0;text-align:center;font-size:13px;line-height:21px}

.tools{top:1475px;height:335px;background:var(--grey-bg);padding-top:64px}
.tool-row{position:absolute;top:131px;left:50px;right:50px;display:flex;justify-content:space-between}
.tool{width:187px;text-align:center}
.tool-box{height:120px;border:3px solid var(--line);background:var(--white);position:relative;display:flex;align-items:center;justify-content:center}
.tool-box::before{content:"";position:absolute;top:-3px;left:73px;width:36px;height:5px;background:var(--green)}
.tool h3{margin-top:18px;font-size:15px;font-weight:500;color:var(--ink);text-transform:uppercase}

.services{top:1810px;height:570px;padding-top:82px}
.service-row{position:absolute;top:172px;left:50px;right:50px;display:flex;justify-content:space-between}
.service{width:245px;text-align:center}
.service-icon{width:160px;height:160px;margin:0 auto;border-radius:50%;background:var(--green);border:6px solid #e9f4dc;box-shadow:0 0 0 2px var(--green);display:flex;align-items:center;justify-content:center}
.service h3{margin-top:32px;font-size:15px;font-weight:700;color:var(--ink);text-transform:uppercase;line-height:20px}
.service p{margin-top:12px;font-size:13px;line-height:20px}
.read-more{display:inline-block;margin-top:18px;background:#dcdcdc;color:var(--white);font-size:11px;padding:0 22px;height:26px;line-height:26px;text-transform:uppercase}

.testimonial{top:2380px;height:418px;background:var(--grey-bg);padding-top:80px}
.quote{width:900px;margin:44px auto 0;text-align:center;font-size:14px;line-height:23px}
.quote-author{width:1100px;margin:42px auto 0;border-top:1px solid var(--line);padding-top:18px;text-align:center}
.quote-author strong{display:block;color:#2b63b0;font-weight:600;font-size:15px}
.quote-author span{font-size:12px}

.partners{top:2798px;height:209px;display:flex;justify-content:space-between;padding:36px 50px 0}
.partner{width:160px;height:95px;border:1px solid #ddd;display:flex;align-items:center;justify-content:center;font-family:"Ubuntu",sans-serif;font-weight:700;font-size:16px;color:#444}

/* footer */
.site-footer{top:3007px;height:334px;background:var(--footer);color:#cfd5dc}
.foot-cols{position:absolute;top:46px;left:50px;right:50px;display:flex}
.foot-col{width:220px}
.foot-col h4{font-size:15px;font-weight:700;color:var(--white);text-transform:uppercase;margin-bottom:16px}
.foot-col li{list-style:none;font-size:12px;line-height:33px;display:flex;align-items:center;gap:10px}
.social-dot{width:36px;height:36px;border-radius:50%;background:var(--white);display:inline-block}
.store{width:116px;height:40px;border-radius:6px;background:#000;border:1px solid #666;margin-bottom:12px}
.foot-bar{position:absolute;bottom:0;left:0;right:0;height:34px;background:var(--footer-bar);font-size:12px;display:flex;justify-content:space-between;align-items:center;padding:0 50px;color:#aab}
</style>
</head>
<body>

<header class="site-header">
  <a class="brand" href="#"><span class="brand-mark"></span><span class="brand-name">Maplecourt Link</span></a>
  <nav class="top-links"><a href="#">Home</a>|<a href="#">About Us</a>|<a href="#">FAQ</a>|<a href="#">Contact</a></nav>
  <div class="login">
    <a class="btn btn-green" href="#">Affiliate Login</a>
    <a class="btn btn-navy" href="#">Merchant Login</a>
  </div>
  <nav class="main-nav">
    <a class="active" href="#">Popular Merchants</a>
    <a href="#">Green Merchants</a>
    <a href="#">Business Merchants</a>
    <a href="#">Promotional Tools</a>
    <a href="#">Offers</a>
    <a href="#">Intergration</a>
    <a href="#">Features</a>
    <a href="#">More Merchants</a>
  </nav>
</header>

<section class="hero">
  <h1 class="hero-title">HOW <span>AFFILIATE MARKETING</span> WORKS</h1>
  <svg class="hero-lines" width="1200" height="649" aria-hidden="true">
    <g stroke="rgba(255,255,255,.45)" stroke-width="2" fill="none">
      <path d="M600 395 Q460 260 323 203"/><path d="M600 395 Q380 330 145 320"/><path d="M600 395 Q460 470 320 451"/>
      <path d="M600 395 Q740 260 885 203"/><path d="M600 395 Q820 330 1052 320"/><path d="M600 395 Q740 470 880 451"/>
    </g>
  </svg>
  <div class="hub" role="img" aria-label="Illustration of natural product jar and oil bottle at the centre"></div>

  <div class="node" style="left:256px;top:136px"><div class="fill" role="img" aria-label="Social media icons illustration" style="background:linear-gradient(135deg,#3b6fc4,#e04a3a)"></div></div>
  <div class="node" style="left:78px;top:253px"><div class="fill" role="img" aria-label="Blog badge illustration" style="background:#f08a1c"></div></div>
  <div class="node" style="left:253px;top:384px"><div class="fill" role="img" aria-label="Presentation board illustration" style="background:linear-gradient(#e8e8e8,#c94040)"></div></div>

  <div class="node" style="left:818px;top:136px">
    <svg width="80" height="80" viewBox="0 0 80 80" aria-label="Phone"><circle cx="40" cy="40" r="38" fill="#2aa0d8"/><path d="M28 22c3 0 5 7 5 9s-3 3-3 4c1 5 7 11 12 12 1 0 2-3 4-3s9 2 9 5-3 8-8 8C35 57 23 45 23 30c0-5 2-8 5-8z" fill="#fff"/></svg>
  </div>
  <div class="node" style="left:985px;top:253px">
    <svg width="80" height="80" viewBox="0 0 80 80" aria-label="Chat"><rect x="6" y="10" width="68" height="56" rx="14" fill="#3fb63a"/><rect x="18" y="22" width="44" height="28" rx="8" fill="#fff"/><path d="M26 50l-6 10 14-10z" fill="#fff"/></svg>
  </div>
  <div class="node" style="left:813px;top:384px">
    <svg width="80" height="80" viewBox="0 0 80 80" aria-label="Envelope"><rect x="10" y="20" width="60" height="40" fill="#fff" stroke="#333" stroke-width="3"/><path d="M10 20l30 24 30-24" fill="none" stroke="#333" stroke-width="3"/></svg>
  </div>

  <a class="hero-cta" href="#">Get Started Now!</a>
</section>

<section class="programs">
  <div class="program program-affiliate">
    <h2>Welcome to Affiliate Program</h2>
    <p>Join a network of natural product promoters and earn on every sale you refer. Share products you trust through your blog, social pages and email, and track every click from one simple dashboard. Sign up today and start earning in minutes.</p>
    <a class="btn" href="#">Affiliate Sign Up</a>
  </div>
  <div class="program program-merchant">
    <h2>Welcome to Merchant Program</h2>
    <p>Reach sales reps, bloggers and social marketers who love natural products. List your goods, set your commission and let our affiliates spread the word while you pay only for results. Our tools make launching a program quick and easy.</p>
    <a class="btn" href="#">Merchant Sign Up</a>
  </div>
</section>

<section class="welcome">
  <h2 class="sec-title">Welcome to Maplecourt Link</h2>
  <p>Maplecourt Link brings natural product makers and the people who promote them together in one place. Merchants list their products and set fair commissions, while affiliates choose the brands they believe in and share them with their readers, followers and customers. Every click, lead and sale is tracked in real time, and payouts arrive on schedule. Whether you run a small herbal shop, write a wellness blog or manage a team of sales reps, our platform gives you the tools, reports and support you need to grow your income and reach.</p>
</section>

<section class="tools">
  <h2 class="sec-title">We Build Tools to Help Our Clients Succeed in Affiliate Marketing</h2>
  <div class="tool-row">
    <div class="tool"><div class="tool-box">
      <svg width="70" height="70" viewBox="0 0 70 70" aria-label="Tools"><g fill="#3f9a1a"><rect x="31" y="4" width="8" height="62" rx="3" transform="rotate(45 35 35)"/><rect x="31" y="4" width="8" height="62" rx="3" transform="rotate(-45 35 35)"/><circle cx="14" cy="14" r="10"/><circle cx="56" cy="56" r="8"/></g></svg>
    </div><h3>Technology</h3></div>
    <div class="tool"><div class="tool-box">
      <svg width="76" height="70" viewBox="0 0 76 70" aria-label="Gears"><g fill="none" stroke="#3f9a1a" stroke-width="9" stroke-dasharray="6 4"><circle cx="28" cy="40" r="17"/><circle cx="56" cy="20" r="10"/></g><circle cx="28" cy="40" r="6" fill="#3f9a1a"/><circle cx="56" cy="20" r="4" fill="#3f9a1a"/></svg>
    </div><h3>Services</h3></div>
    <div class="tool"><div class="tool-box">
      <svg width="64" height="64" viewBox="0 0 80 80" aria-label="Phone"><path d="M22 8c4 0 8 11 8 14s-5 5-5 7c2 9 14 21 24 24 2 0 4-5 7-5s14 4 14 8-4 14-12 14C33 70 10 47 10 22c0-8 6-14 12-14z" fill="#3f9a1a"/></svg>
    </div><h3>About Us</h3></div>
    <div class="tool"><div class="tool-box">
      <svg width="70" height="64" viewBox="0 0 70 64" aria-label="Speech bubble"><ellipse cx="35" cy="28" rx="32" ry="24" fill="#3f9a1a"/><path d="M14 44l-6 16 20-12z" fill="#3f9a1a"/></svg>
    </div><h3>Our Blog</h3></div>
  </div>
</section>

<section class="services">
  <h2 class="sec-title">Maplecourt Link Services</h2>
  <div class="service-row">
    <div class="service">
      <div class="service-icon"><svg width="70" height="80" viewBox="0 0 70 80" aria-label="Money bag"><path d="M25 8h20l-6 12h-8z" fill="#fff"/><path d="M31 20h8c18 10 26 26 26 40 0 10-10 16-30 16S5 70 5 60c0-14 8-30 26-40z" fill="#fff"/><text x="35" y="64" text-anchor="middle" font-family="Ubuntu,sans-serif" font-weight="700" font-size="28" fill="#5ca61c">$</text></svg></div>
      <h3>Earn up to 50% Commission<br>for all Products!</h3>
      <p>Not only can you join our team and help spread the word about your favorite products, you can get rewarded...</p>
      <a class="read-more" href="#">Read More</a>
    </div>
    <div class="service">
      <div class="service-icon"><svg width="64" height="74" viewBox="0 0 64 74" aria-label="Database"><g fill="#fff"><ellipse cx="32" cy="10" rx="28" ry="9"/><path d="M4 18c0 5 12 9 28 9s28-4 28-9v12c0 5-12 9-28 9S4 35 4 30z"/><path d="M4 38c0 5 12 9 28 9s28-4 28-9v12c0 5-12 9-28 9S4 55 4 50z"/><path d="M4 58c0 5 12 9 28 9s28-4 28-9v6c0 5-12 9-28 9S4 69 4 64z"/></g></svg></div>
      <h3>High Conversion Rate =<br>More Money</h3>
      <p>Our website and plans generate one of the highest conversion rates in the industry. Our high conversion rates mean...</p>
      <a class="read-more" href="#">Read More</a>
    </div>
    <div class="service">
      <div class="service-icon"><svg width="80" height="64" viewBox="0 0 80 64" aria-label="Savings"><ellipse cx="38" cy="34" rx="30" ry="22" fill="#fff"/><rect x="18" y="48" width="9" height="14" fill="#fff"/><rect x="48" y="48" width="9" height="14" fill="#fff"/><rect x="66" y="28" width="10" height="10" rx="3" fill="#fff"/><rect x="30" y="13" width="16" height="4" fill="#5ca61c"/></svg></div>
      <h3>Long Cookie<br>Duration</h3>
      <p>If a customer comes from your site to ours, and then comes back to purchase six months later, you get credit.</p>
      <a class="read-more" href="#">Read More</a>
    </div>
    <div class="service">
      <div class="service-icon"><svg width="70" height="70" viewBox="0 0 70 70" aria-label="Question"><circle cx="35" cy="35" r="32" fill="none" stroke="#fff" stroke-width="5"/><text x="35" y="50" text-anchor="middle" font-family="Ubuntu,sans-serif" font-weight="700" font-size="42" fill="#fff">?</text></svg></div>
      <h3>How Does It<br>Work?</h3>
      <p>It couldn't be simpler! We've streamlined our entire affiliate process to ensure ease of use, while still maintaining...</p>
      <a class="read-more" href="#">Read More</a>
    </div>
  </div>
</section>

<section class="testimonial">
  <h2 class="sec-title">What Our Client's Say</h2>
  <p class="quote">“Signing up took minutes and the first commission arrived within weeks. The dashboard is clear, the products are ones I already use, and the support team answers every question quickly. I recommend this program to any wellness blogger.”</p>
  <div class="quote-author"><strong>Dana Halvers</strong><span>Cedar Fork Cabin Stays</span></div>
</section>

<section class="partners">
  <div class="partner">Korvane Electric</div>
  <div class="partner">Tessaro</div>
  <div class="partner">Ventaro Air</div>
  <div class="partner">Lumisonic</div>
  <div class="partner">Arvel</div>
  <div class="partner">Ledgerly</div>
</section>

<footer class="site-footer">
  <div class="foot-cols">
    <div class="foot-col"><h4>About Us</h4><ul><li>Company</li><li>Contact us</li><li>Privacy Policy</li></ul></div>
    <div class="foot-col"><h4>Affiliates</h4><ul><li>Affiliates Information</li><li>Affiliate link formats</li></ul></div>
    <div class="foot-col"><h4>Merchants</h4><ul><li>Merchants Login</li><li>Integration methods</li><li>API Reference</li><li>Samples and Tests</li><li>Quill Partner Pro</li></ul></div>
    <div class="foot-col"><h4>Let's Be Social</h4><ul><li><span class="social-dot"></span>Friendwall</li><li><span class="social-dot"></span>Chirpline</li><li><span class="social-dot"></span>Zorvix+</li></ul></div>
    <div class="foot-col"><h4>Mobile</h4><div class="store" role="img" aria-label="App store badge"></div><div class="store" role="img" aria-label="App store badge"></div></div>
  </div>
  <div class="foot-bar"><span>Copyright © 2014. Maplecourt Link All Right reserved.</span><span>Terms and Conditions</span></div>
</footer>

</body>
</html>
```